Business Card Design Project

I have just chosen a logo and would now like this designed onto a business card for my hair salon. I would like it to be classy not to busy and have a wow factor when people look at them
Has to Include on card:
Logo Design
And business details below
Kellie-ann Drummond (owner)
0482 736 219
Rdw@vomblet.com.au
71 Willowmere Rise Corvin Cove
Logo is now attached please provide designs
Hair

```html
<!DOCTYPE html>
<html lang="en">
<head>
<meta charset="utf-8">
<title>Larkspur Hair House — Business Card</title>
<link rel="stylesheet" href="https://fonts.googleapis.com/css2?family=Cormorant+Garamond:wght@500;600&family=Cinzel:wght@400&display=swap">
<style>
  :root {
    --page: #ffffff;
    --ink-black: #020202;
    --panel-grey: #262626;
    --accent-pink: #ee1a6d;
    --text-white: #f4f4f4;
    --damask-light: #e9e9e9;
    --damask-dark: #5a5a5a;
  }
  html, body {
    margin: 0;
    width: 1200px;
    height: 1000px;
    overflow: hidden;
    background: var(--page);
  }
  .canvas {
    position: relative;
    width: 1200px;
    height: 1000px;
  }
  .card {
    position: absolute;
    background: var(--ink-black);
    box-shadow: 6px 8px 10px rgba(0, 0, 0, 0.35);
    overflow: hidden;
  }
  .damask-fill {
    position: absolute;
    background: linear-gradient(135deg, var(--damask-light), var(--damask-dark) 50%, var(--damask-light));
  }
  .pink-rule {
    position: absolute;
    background: var(--accent-pink);
  }

  /* Front */
  .card-front {
    left: 340px;
    top: 60px;
    width: 436px;
    height: 240px;
  }
  .card-front .damask-fill {
    left: 0; top: 0;
    width: 151px; height: 240px;
  }
  .card-front .pink-rule {
    left: 151px; top: 0;
    width: 12px; height: 240px;
  }
  .owner-name {
    position: absolute;
    left: 163px;
    right: 0;
    top: 18px;
    text-align: center;
    margin: 0;
    font-family: "Cormorant Garamond", serif;
    font-weight: 500;
    font-size: 29px;
    color: var(--text-white);
    letter-spacing: 0.3px;
  }
  .brand-panel {
    position: absolute;
    left: 163px;
    top: 52px;
    width: 273px;
    height: 156px;
    background: var(--panel-grey);
    display: flex;
    align-items: center;
    justify-content: center;
  }
  .brand-name {
    margin: 0;
    font-family: "Cormorant Garamond", serif;
    font-weight: 600;
    font-size: 38px;
    line-height: 1.0;
    text-align: center;
    color: var(--accent-pink);
    letter-spacing: 1px;
    text-transform: uppercase;
  }

  /* Back */
  .card-back {
    left: 426px;
    top: 447px;
    width: 281px;
    height: 493px;
  }
  .contact-list {
    position: absolute;
    left: 0;
    right: 0;
    top: 92px;
    margin: 0;
    padding: 0 4px;
    list-style: none;
    text-align: center;
    font-family: "Cinzel", serif;
    font-size: 19px;
    line-height: 30px;
    color: var(--text-white);
  }
  .card-back .pink-rule {
    left: 0; top: 322px;
    width: 281px; height: 8px;
  }
  .card-back .damask-fill {
    left: 0; top: 330px;
    width: 281px; height: 163px;
  }
</style>
</head>
<body>
<main class="canvas">
  <section class="card card-front" aria-label="Business card front">
    <div class="damask-fill" role="img" aria-label="Black and white damask pattern"></div>
    <div class="pink-rule"></div>
    <h1 class="owner-name">Kellie-ann Drummond</h1>
    <div class="brand-panel">
      <p class="brand-name">Larkspur<br>Hair House</p>
    </div>
  </section>

  <section class="card card-back" aria-label="Business card back">
    <ul class="contact-list">
      <li class="contact-phone">0482 736 219</li>
      <li class="contact-email">Rdw@vomblet.com.au</li>
      <li class="contact-address">71 Willowmere Rise Corvin Cove</li>
    </ul>
    <div class="pink-rule"></div>
    <div class="damask-fill" role="img" aria-label="Black and white damask pattern"></div>
  </section>
</main>
</body>
</html>
```